Label for Whiskey and Rum Bottle

We are a distillery. Whiskey and Rum We like to have a new label for our bottles. The whiskey bottles are in a wooden case. http://www.korntropfen-muster.ch/store/product/tannwalder-oberkamm-single-malt-whiskey-nr-6 The Rum Bottles have no package. The label is even more important. http://www.korntropfen-muster.ch/store/product/tannwalder-oberkämmer-rum You can see the form of the bottles here www.korntropfen-muster.ch/store Whiskey and rum bottles are for a liter (50 cl) The labels can be with a picture or without. We would like to have something completely new. Therefore we don`t like to make much prescriptions concerning the design. We don`t like to give too much information (text) on the label. Just the information required by law. Consumers should understand the labels without long-reading. (The label-text is below) The 2 labels (Whiskey and rum) should look similar. Probably they have a different color or a different picture or .... It should be clear that the 2 products are from the same distillery. We have the intention to change all our existing labels over time. This gives designers the chance for follow-up projects.

Target Market(s)

Adults, liquor lovers

Requirements
Must have
• Information on the label is in German. (See "") Whiskey: - the name of the whiskey is "Tannwald Ridgeside Single Malt Whiskey" - The Whiskey was matured 5 years in a sherry "5 years in the sherry barrel stored" - The Alcohol content is 40% volumes "40% Vol "- The bottle contents 50 cl" 5 dl "- The distillery is" Distillery Brugghofer, Felsmatt, www.korntropfen-muster.ch "- The producer is" Korvix GmbH "Rum: - The name is" Tannwald Ridgesider Rum "- The alcohol content is 37% Volumes "37% Vol" - The bottle contens 50 cl "5 dl" - The distillery is "Distillery Brugghofer, Felsmatt, www.korntropfen-muster.ch" - The producer is "Korvix GmbH"
Nice to have
• Premium looking label Only front label preferred Only necessary text on the label
Should not have
• No special print techniques necessary No special paper form

```html
<!DOCTYPE html>
<html lang="de">
<head>
<meta charset="utf-8">
<title>Tannwalder Oberkämmer Rum – Etikett</title>
<link rel="stylesheet" href="https://fonts.googleapis.com/css2?family=EB+Garamond:wght@400;500&display=swap">
<style>
  :root {
    --label-red: #7b1619;
    --label-gold: #c9a84f;
    --label-white: #ffffff;
    --page-bg: #ffffff;
    --copper: #a4532a;
    --still-dark: #3a1a14;
    --glass-amber: #d8c68c;
    --glass-pale: #eee4c2;
  }
  * { box-sizing: border-box; margin: 0; padding: 0; }
  html, body { width: 1200px; height: 900px; overflow: hidden; background: var(--page-bg); }
  .canvas { position: relative; width: 1200px; height: 900px; font-family: "EB Garamond", Georgia, serif; }

  .label {
    position: absolute; left: 109px; top: 22px; width: 635px; height: 846px;
    background: var(--label-red); color: var(--label-white);
  }
  .label__frame { position: absolute; left: 0; top: 0; width: 635px; height: 320px; }

  .label__title {
    position: absolute; left: 0; right: 0; top: 182px; text-align: center;
    color: var(--label-gold); font-size: 54px; font-weight: 500; line-height: 1;
    letter-spacing: 0.3px;
  }
  .label__kind {
    position: absolute; left: 0; right: 0; top: 240px; text-align: center;
    color: var(--label-gold); font-size: 29px; font-weight: 400; line-height: 1;
  }

  .label__still {
    position: absolute; left: 284px; top: 557px; width: 66px; height: 133px;
    background: linear-gradient(180deg, var(--copper) 0%, var(--copper) 65%, var(--still-dark) 100%);
  }

  .label__brand {
    position: absolute; left: 0; right: 0; top: 701px; text-align: center;
    font-size: 22px; font-weight: 400; line-height: 24px; letter-spacing: 1px;
    text-transform: uppercase;
  }
  .label__address {
    position: absolute; left: 0; right: 0; top: 762px; text-align: center;
    font-size: 15px; line-height: 19px; letter-spacing: 2.2px;
  }
  .label__abv, .label__volume {
    position: absolute; top: 784px; font-size: 21px; line-height: 1;
  }
  .label__abv { left: 37px; }
  .label__volume { right: 41px; }

  .bottle-photo {
    position: absolute; left: 830px; top: 212px; width: 179px; height: 434px;
    background: linear-gradient(180deg, var(--label-red) 0%, var(--label-red) 25%, var(--glass-pale) 32%, var(--glass-amber) 42%, var(--label-red) 44%, var(--label-red) 96%, var(--glass-amber) 100%);
  }
</style>
</head>
<body>
<main class="canvas">
  <section class="label" aria-label="Flaschenetikett Tannwalder Oberkämmer Rum">
    <svg class="label__frame" viewBox="0 0 635 320">
      <path d="M67 159 Q318 120 570 159" fill="none" stroke="var(--label-white)" stroke-width="2"/>
      <path d="M207 157 Q318 146 428 157" fill="none" stroke="var(--label-white)" stroke-width="1.6"/>
      <rect role="img" aria-label="Verziertes Zierornament über dem Produktnamen" x="230" y="76" width="176" height="57" rx="22" fill="var(--label-white)" opacity="0.18"/>
      <line x1="70" y1="292" x2="216" y2="292" stroke="var(--label-white)" stroke-width="2"/>
      <line x1="423" y1="292" x2="564" y2="292" stroke="var(--label-white)" stroke-width="2"/>
      <rect role="img" aria-label="Geschwungenes Trennornament" x="216" y="284" width="207" height="18" rx="9" fill="var(--label-white)" opacity="0.18"/>
    </svg>

    <h1 class="label__title">Tannwalder Oberkämmer</h1>
    <p class="label__kind">Rum</p>

    <div class="label__still" role="img" aria-label="Illustration einer kupfernen Brennblase"></div>

    <p class="label__brand">Brennerei<br>Brugghofer</p>

    <p class="label__address">Brennerei Brugghofer, Felsmatt<br>www.korntropfen-muster.ch<br>Korvix GmbH</p>

    <p class="label__abv">37%Vol</p>
    <p class="label__volume">50 cl</p>
  </section>

  <div class="bottle-photo" role="img" aria-label="Foto der Rumflasche mit aufgeklebtem Etikett"></div>
</main>
</body>
</html>
```